Custom Woodworking and Rock Design

We specialize in original, high quality, wood and rock art. It’s should be self explanatory ask questions if you need. Your team designing a logo. Furniture is custom made to order. Rocks are designed depending on consumer needs. Wood and rock can also be combined for custom work. Painted rocks on vintage wood. Custom chairs and cabinets. Artistic rocks for multiple uses:garden, magnets, custom. All ideas and requests are welcome.

Target Market(s)

All

Contact Information for Business Card

Mara Dolby
Talverstonecraft@mailvoro.net

Font styles to use
Sans Serif

Requirements
Must have
• Clear lettering
Nice to have
• Eye catching
Should not have
• Blurr

```html
<!DOCTYPE html>
<html lang="en">
<head>
<meta charset="utf-8">
<title>Talver – Business Card</title>
<link rel="stylesheet" href="https://fonts.googleapis.com/css2?family=Bebas+Neue&display=swap">
<style>
  :root {
    --page: #ffffff;
    --card: #858589;
    --ink-light: #ffffff;
    --brand: #7a5c3a;
    --icon-ink: #858589;
  }
  * { margin: 0; padding: 0; box-sizing: border-box; }
  html, body {
    width: 1200px;
    height: 431px;
    overflow: hidden;
    background: var(--page);
  }
  .canvas {
    position: relative;
    width: 1200px;
    height: 431px;
    font-family: "Bebas Neue", "Oswald", sans-serif;
  }
  .card {
    position: absolute;
    top: 57px;
    width: 514px;
    height: 334px;
    background: var(--card);
  }
  .card--front { left: 38px; }
  .card--back { left: 648px; }

  .brand-name {
    position: absolute;
    color: var(--brand);
    letter-spacing: 0.18em;
    line-height: 1;
  }
  .card--front .brand-name {
    left: 95px;
    top: 95px;
    font-size: 48px;
  }
  .card--back .brand-name {
    left: 0;
    right: 0;
    top: 128px;
    text-align: center;
    font-size: 72px;
  }

  .person {
    position: absolute;
    left: 57px;
    top: 233px;
    color: var(--ink-light);
  }
  .person__name {
    font-size: 48px;
    line-height: 1;
    letter-spacing: 0.01em;
  }
  .person__role {
    margin-top: 2px;
    font-size: 10px;
    letter-spacing: 0.42em;
    text-align: center;
  }

  .contact {
    position: absolute;
    right: 38px;
    top: 233px;
    list-style: none;
    color: var(--ink-light);
  }
  .contact__item {
    display: flex;
    align-items: center;
    justify-content: flex-end;
    gap: 8px;
    height: 24px;
    margin-bottom: 8px;
    font-size: 13px;
    letter-spacing: 0.02em;
  }
  .contact__icon {
    width: 22px;
    height: 22px;
    border-radius: 50%;
    background: var(--ink-light);
    color: var(--icon-ink);
    display: flex;
    align-items: center;
    justify-content: center;
    font-family: Arial, sans-serif;
    font-size: 15px;
    font-weight: bold;
  }
</style>
</head>
<body>
<main class="canvas">
  <section class="card card--front">
    <h1 class="brand-name">Talver</h1>

    <div class="person">
      <p class="person__name">MARA DOLBY</p>
      <p class="person__role">ROCK DESIGNS</p>
    </div>

    <ul class="contact">
      <li class="contact__item">
        <span>TALVERSTONECRAFT@MAILVORO.NET</span>
        <span class="contact__icon" aria-hidden="true">@</span>
      </li>
      <li class="contact__item">
        <span>QUARRY LANE BRENHOLT 90412</span>
        <span class="contact__icon" aria-hidden="true">
          <svg width="12" height="14" viewBox="0 0 12 14">
            <path d="M6 0C2.7 0 0 2.6 0 5.8 0 9.8 6 14 6 14s6-4.2 6-8.2C12 2.6 9.3 0 6 0z" fill="var(--icon-ink)"/>
            <circle cx="6" cy="5.6" r="2.2" fill="#ffffff"/>
          </svg>
        </span>
      </li>
    </ul>
  </section>

  <section class="card card--back">
    <p class="brand-name">Talver</p>
  </section>
</main>
</body>
</html>
```